Business card update

Opening a subsidiary of my company in the USA and need to update my logo.
Updates

I made a mistake on my briefing. It's only the business card. Thanks for alerting me on the mistake.

All the best

Gustavo

Target Market(s)

We are an Executive Search company and our target audience are executives in large corporations.

Industry/Entity Type

Business

Requirements
Must have
• Keep the logo. In the US the company is called Dario Kellner Executive Search.

```html
<!DOCTYPE html>
<html lang="en">
<head>
<meta charset="utf-8">
<title>Dario Kellner Executive Search – Business Card</title>
<link rel="stylesheet" href="https://fonts.googleapis.com/css2?family=Lato:wght@400;700&display=swap">
<style>
  :root {
    --backdrop: #e9e4de;
    --card: #ffffff;
    --ink: #161616;
    --teal: #2aa8b8;
    --teal-pale: #d3ebee;
    --band-light: #3f8194;
    --band-dark: #1d3c48;
    --pill-light: #3a7384;
    --pill-dark: #17323d;
    --on-dark: #ffffff;
  }
  * { margin: 0; padding: 0; box-sizing: border-box; }
  html, body {
    width: 1200px; height: 840px; overflow: hidden;
    background: var(--backdrop);
    font-family: "Lato", sans-serif;
    color: var(--ink);
  }
  .business-card {
    position: absolute; left: 100px; top: 134px;
    width: 1000px; height: 572px;
    background: var(--card);
    box-shadow: 0 10px 30px rgba(0,0,0,.18);
    overflow: hidden;
  }
  .brand {
    position: absolute; top: 96px; left: 0; width: 100%;
    display: flex; justify-content: center; align-items: center; gap: 16px;
  }
  .brand-dot { width: 22px; height: 22px; border-radius: 50%; background: var(--teal); }
  .brand-name {
    font-weight: 700; font-size: 40px; letter-spacing: 1px; color: var(--ink);
  }
  .holder {
    position: absolute; top: 232px; left: 0; width: 100%; text-align: center;
  }
  .holder-name { font-weight: 700; font-size: 38px; line-height: 1.1; }
  .holder-title { font-size: 29px; color: var(--teal); line-height: 1.15; }
  .address {
    position: absolute; left: 58px; top: 372px;
    font-size: 29px; line-height: 1.3;
  }
  .contacts {
    position: absolute; left: 496px; top: 352px;
    font-size: 29px; line-height: 1.3;
  }
  .contact-line { display: flex; align-items: center; gap: 12px; height: 42px; }
  .contact-icon { width: 30px; height: 30px; fill: var(--band-dark); }
  .accent-stripe {
    position: absolute; left: 0; bottom: 70px; width: 100%; height: 10px;
    background: var(--teal-pale);
  }
  .footer-band {
    position: absolute; left: 0; bottom: 0; width: 100%; height: 70px;
    background: linear-gradient(90deg, var(--band-light), var(--band-dark));
  }
  .web-pill {
    position: absolute; left: 280px; top: 458px;
    height: 54px; padding: 0 16px 0 24px;
    display: flex; align-items: center; gap: 18px;
    border-radius: 27px;
    background: linear-gradient(180deg, var(--pill-light), var(--pill-dark));
    box-shadow: 0 4px 8px rgba(0,0,0,.3);
    color: var(--on-dark); font-size: 29px;
  }
  .web-arrow {
    border-left: 1px solid rgba(255,255,255,.45);
    padding-left: 12px; height: 34px; display: flex; align-items: center;
  }
  .web-arrow svg { width: 22px; height: 22px; }
</style>
</head>
<body>
  <article class="business-card">
    <header class="brand">
      <span class="brand-dot"></span>
      <span class="brand-name">Dario Kellner Executive Search</span>
    </header>

    <section class="holder">
      <h1 class="holder-name">Gustavo S. Kellner</h1>
      <p class="holder-title">chief executive officer</p>
    </section>

    <address class="address" style="font-style:normal">
      4820 Harbor Point Blvd Suite 310<br>
      Coral Bay FL 33190
    </address>

    <div class="contacts">
      <div class="contact-line">
        <svg class="contact-icon" viewBox="0 0 24 24" aria-hidden="true">
          <path d="M6.6 10.8a15.1 15.1 0 0 0 6.6 6.6l2.2-2.2a1 1 0 0 1 1-.25 11.4 11.4 0 0 0 3.6.57 1 1 0 0 1 1 1V20a1 1 0 0 1-1 1A17 17 0 0 1 3 4a1 1 0 0 1 1-1h3.5a1 1 0 0 1 1 1c0 1.25.2 2.45.57 3.57a1 1 0 0 1-.25 1z"/>
        </svg>
        <span>305 555-0147</span>
      </div>
      <div class="contact-line">
        <svg class="contact-icon" viewBox="0 0 24 24" aria-hidden="true">
          <rect x="2" y="5" width="20" height="14" rx="1"/>
          <polyline points="2.5,5.5 12,13 21.5,5.5" fill="none" stroke="#ffffff" stroke-width="1.5"/>
        </svg>
        <span>gkellner@dkexecutivesearch.com</span>
      </div>
    </div>

    <div class="accent-stripe"></div>
    <div class="footer-band"></div>

    <div class="web-pill">
      <span>www.dkexecutivesearch.com</span>
      <span class="web-arrow">
        <svg viewBox="0 0 24 24" aria-hidden="true">
          <polyline points="8,4 16,12 8,20" fill="none" stroke="#ffffff" stroke-width="4" stroke-linecap="round" stroke-linejoin="round"/>
        </svg>
      </span>
    </div>
  </article>
</body>
</html>
```